Banner Ad Design

Need design of small banners for page margins on a Printing website that is currently under development. Need designs for these 4 promo items:

Table Tents (1000): $217
Flyers (5000): $328
Postcards (5000): $237
Brochures (5000): $386

Use the same detail text that is shown in the attached examples - such as "Full Color Front 14 pt, etc, etc". Pricing and quantity should be as provided above.

Color scheme and images should also be similar to what is shown. Banner sizes should be 120 x 120.

Printing

```html
<!DOCTYPE html>
<html lang="en">
<head>
<meta charset="utf-8">
<title>Print Specials Banners</title>
<link rel="stylesheet" href="https://fonts.googleapis.com/css2?family=Arimo:wght@400;700&family=Open+Sans:wght@700;800&display=swap">
<style>
  :root {
    --bg-dark: #1c1c1c;
    --bg-mid: #2e2e2e;
    --tile-top: #ffffff;
    --tile-bottom: #e2e2e2;
    --detail: #555555;
    --qty: #6a6a6a;
    --ribbon-orange: #f07818;
    --ribbon-pink: #e8186a;
    --ribbon-blue: #2a8ee0;
    --ribbon-purple: #b82ad8;
    --title-orange: #f07818;
    --title-blue: #1a88d0;
    --title-red: #e01818;
    --title-purple: #9a1aa8;
    --oval-green: #8cc43c;
    --oval-blue: #1a6ad8;
    --oval-red: #d81818;
    --oval-cyan: #2ad6d6;
    --photo-a: #d9a070;
    --photo-b: #2a2a2a;
  }
  * { box-sizing: border-box; margin: 0; padding: 0; }
  html, body { width: 1200px; height: 900px; overflow: hidden; }
  body {
    background: radial-gradient(ellipse at 50% 45%, var(--bg-mid) 0%, var(--bg-dark) 75%);
    position: relative;
    font-family: "Arimo", Arial, sans-serif;
  }
  .tile {
    position: absolute;
    width: 118px;
    height: 114px;
  }
  .tile-card {
    position: absolute;
    inset: 0;
    border-radius: 8px;
    overflow: hidden;
    background: linear-gradient(to bottom, var(--tile-top) 0%, var(--tile-bottom) 100%);
    box-shadow: 0 1px 3px rgba(0,0,0,.5);
  }
  .ribbon {
    position: absolute;
    left: -24px;
    top: 13px;
    width: 82px;
    height: 17px;
    transform: rotate(-45deg);
    background: var(--ribbon);
    color: #fff;
    font: 700 10px/17px "Arimo", Arial, sans-serif;
    text-align: center;
  }
  .product-photo {
    position: absolute;
    top: 2px;
    right: 3px;
    width: 76px;
    height: 34px;
    background: linear-gradient(100deg, var(--photo-b) 0%, var(--photo-b) 40%, var(--photo-a) 70%, #f2e2d0 100%);
    border-radius: 2px;
  }
  .photo-brochure { width: 60px; height: 36px; right: 2px; background: linear-gradient(160deg, #f0dcc8 0%, var(--photo-a) 55%, var(--photo-b) 100%); }
  .photo-tent { width: 34px; height: 42px; right: 12px; top: 0; background: linear-gradient(150deg, #ece4dc 0%, var(--photo-a) 45%, var(--photo-b) 100%); }
  .details {
    position: absolute;
    left: 4px;
    top: 45px;
    font-size: 8.5px;
    line-height: 9.5px;
    color: var(--detail);
    white-space: nowrap;
  }
  .row-flyer .details { top: 46px; }
  .title {
    position: absolute;
    left: 4px;
    top: 65px;
    font: 700 16px/16px "Arimo", Arial, sans-serif;
    letter-spacing: -0.3px;
    color: var(--title);
    -webkit-text-stroke: 0.4px var(--title);
    white-space: nowrap;
  }
  .row-flyer .title { top: 69px; }
  .qty {
    position: absolute;
    left: 4px;
    bottom: 6px;
    font: 700 15px/16px "Arimo", Arial, sans-serif;
    color: var(--qty);
  }
  .qty small { font-size: 8px; font-weight: 400; margin-left: 2px; }
  .price {
    position: absolute;
    left: 55px;
    bottom: -4px;
    width: 60px;
    height: 36px;
    border-radius: 50%;
    background: radial-gradient(ellipse at 50% 25%, rgba(255,255,255,.45) 0%, rgba(255,255,255,0) 55%), var(--oval);
    border: 1.5px solid rgba(255,255,255,.85);
    color: #fff;
    font: 800 18px/33px "Open Sans", Arial, sans-serif;
    text-align: center;
    letter-spacing: -0.5px;
    text-shadow: 0 1px 1px rgba(0,0,0,.35);
  }
  .col-1 { left: 265px; --ribbon: var(--ribbon-orange); --title: var(--title-orange); --oval: var(--oval-green); }
  .col-2 { left: 445px; --ribbon: var(--ribbon-pink); --title: var(--title-blue); --oval: var(--oval-blue); }
  .col-3 { left: 625px; --ribbon: var(--ribbon-blue); --title: var(--title-red); --oval: var(--oval-red); }
  .col-4 { left: 805px; --ribbon: var(--ribbon-purple); --title: var(--title-purple); --oval: var(--oval-cyan); }
  .row-flyer { top: 78px; }
  .row-postcard { top: 275px; }
  .row-brochure { top: 462px; }
  .row-tent { top: 659px; }
</style>
</head>
<body>
<main class="banner-sheet">

  <section class="tile row-flyer col-1"><div class="tile-card"><div class="product-photo" role="img" aria-label="Stack of printed flyers"></div><div class="ribbon">Special</div><p class="details">Full Color Front<br>100 lb Gloss + AQ</p><h2 class="title">Flyers</h2><p class="qty">5000<small>for</small></p></div><div class="price">$328</div></section>
  <section class="tile row-flyer col-2"><div class="tile-card"><div class="product-photo" role="img" aria-label="Stack of printed flyers"></div><div class="ribbon">Special</div><p class="details">Full Color Front<br>100 lb Gloss + AQ</p><h2 class="title">Flyers</h2><p class="qty">5000<small>for</small></p></div><div class="price">$328</div></section>
  <section class="tile row-flyer col-3"><div class="tile-card"><div class="product-photo" role="img" aria-label="Stack of printed flyers"></div><div class="ribbon">Special</div><p class="details">Full Color Front<br>100 lb Gloss + AQ</p><h2 class="title">Flyers</h2><p class="qty">5000<small>for</small></p></div><div class="price">$328</div></section>
  <section class="tile row-flyer col-4"><div class="tile-card"><div class="product-photo" role="img" aria-label="Stack of printed flyers"></div><div class="ribbon">Special</div><p class="details">Full Color Front<br>100 lb Gloss + AQ</p><h2 class="title">Flyers</h2><p class="qty">5000<small>for</small></p></div><div class="price">$328</div></section>

  <section class="tile row-postcard col-1"><div class="tile-card"><div class="product-photo" role="img" aria-label="Fanned printed postcards"></div><div class="ribbon">Special</div><p class="details">Full Color Front<br>14pt with UV Coating</p><h2 class="title">Postcards</h2><p class="qty">5000<small>for</small></p></div><div class="price">$237</div></section>
  <section class="tile row-postcard col-2"><div class="tile-card"><div class="product-photo" role="img" aria-label="Fanned printed postcards"></div><div class="ribbon">Special</div><p class="details">Full Color Front<br>14pt with UV Coating</p><h2 class="title">Postcards</h2><p class="qty">5000<small>for</small></p></div><div class="price">$237</div></section>
  <section class="tile row-postcard col-3"><div class="tile-card"><div class="product-photo" role="img" aria-label="Fanned printed postcards"></div><div class="ribbon">Special</div><p class="details">Full Color Front<br>14pt with UV Coating</p><h2 class="title">Postcards</h2><p class="qty">5000<small>for</small></p></div><div class="price">$237</div></section>
  <section class="tile row-postcard col-4"><div class="tile-card"><div class="product-photo" role="img" aria-label="Fanned printed postcards"></div><div class="ribbon">Special</div><p class="details">Full Color Front<br>14pt with UV Coating</p><h2 class="title">Postcards</h2><p class="qty">5000<small>for</small></p></div><div class="price">$237</div></section>

  <section class="tile row-brochure col-1"><div class="tile-card"><div class="product-photo photo-brochure" role="img" aria-label="Open tri-fold brochure"></div><div class="ribbon">Special</div><p class="details">Full Color<br>8.5"x11" Tri-Fold</p><h2 class="title">Brochures</h2><p class="qty">5000<small>for</small></p></div><div class="price">$386</div></section>
  <section class="tile row-brochure col-2"><div class="tile-card"><div class="product-photo photo-brochure" role="img" aria-label="Open tri-fold brochure"></div><div class="ribbon">Special</div><p class="details">Full Color<br>8.5"x11" Tri-Fold</p><h2 class="title">Brochures</h2><p class="qty">5000<small>for</small></p></div><div class="price">$386</div></section>
  <section class="tile row-brochure col-3"><div class="tile-card"><div class="product-photo photo-brochure" role="img" aria-label="Open tri-fold brochure"></div><div class="ribbon">Special</div><p class="details">Full Color<br>8.5"x11" Tri-Fold</p><h2 class="title">Brochures</h2><p class="qty">5000<small>for</small></p></div><div class="price">$386</div></section>
  <section class="tile row-brochure col-4"><div class="tile-card"><div class="product-photo photo-brochure" role="img" aria-label="Open tri-fold brochure"></div><div class="ribbon">Special</div><p class="details">Full Color<br>8.5"x11" Tri-Fold</p><h2 class="title">Brochures</h2><p class="qty">5000<small>for</small></p></div><div class="price">$386</div></section>

  <section class="tile row-tent col-1"><div class="tile-card"><div class="product-photo photo-tent" role="img" aria-label="Folded table tent card"></div><div class="ribbon">Special</div><p class="details">Full Color Front<br>14pt with UV Coating</p><h2 class="title">Table Tents</h2><p class="qty">1000<small>for</small></p></div><div class="price">$217</div></section>
  <section class="tile row-tent col-2"><div class="tile-card"><div class="product-photo photo-tent" role="img" aria-label="Folded table tent card"></div><div class="ribbon">Special</div><p class="details">Full Color Front<br>14pt with UV Coating</p><h2 class="title">Table Tents</h2><p class="qty">1000<small>for</small></p></div><div class="price">$217</div></section>
  <section class="tile row-tent col-3"><div class="tile-card"><div class="product-photo photo-tent" role="img" aria-label="Folded table tent card"></div><div class="ribbon">Special</div><p class="details">Full Color Front<br>14pt with UV Coating</p><h2 class="title">Table Tents</h2><p class="qty">1000<small>for</small></p></div><div class="price">$217</div></section>
  <section class="tile row-tent col-4"><div class="tile-card"><div class="product-photo photo-tent" role="img" aria-label="Folded table tent card"></div><div class="ribbon">Special</div><p class="details">Full Color Front<br>14pt with UV Coating</p><h2 class="title">Table Tents</h2><p class="qty">1000<small>for</small></p></div><div class="price">$217</div></section>

</main>
</body>
</html>
```